Harbor Nightclub

Nightclub flyer., digital single sided, for KV and PX. I included samples of some previous flyers we've used. Sample Info:
HARBOR
FRIDAYS
FRI MAY 1 2020
DJ VORTAN (club floor)
DJ RUZO & DJ TAV (residents on the lounge floor)
4217 Marlow Avenue Sacramento
www.harborvenuehall.example for list/VIP inquiries

Target Market(s)

Upscale top 40 crowd but want some cool and artsy like the examples included.

Font styles to use
Sans Serif

Requirements
Must have
• Harbor Logo
Nice to have
• Would be nice if the flyer can be incorporated later with DJ photos (sometimes we will add dj photos to pixagram etc). Would like a big city type of feel.
Should not have
• Nothing too sexual.

```html
<!DOCTYPE html>
<html lang="en">
<head>
<meta charset="utf-8">
<title>Harbor Nightclub – Friday</title>
<link rel="stylesheet" href="https://fonts.googleapis.com/css2?family=Josefin+Sans:wght@300;400&display=swap">
<style>
  :root {
    --page: #ffffff;
    --night: #04030c;
    --sky-top: #0a0716;
    --sky-mid: #1a1646;
    --ridge: #22308e;
    --nebula: #4a2a78;
    --ink: #ffffff;
    --gold: #e8df6c;
    --rule: #2a46b8;
    --band: #0a0818;
  }
  * { margin: 0; padding: 0; box-sizing: border-box; }
  html, body {
    width: 881px; height: 1200px; overflow: hidden;
    background: var(--page);
  }
  .flyer {
    position: absolute; left: 48px; top: 13px;
    width: 784px; height: 1174px; overflow: hidden;
    background: var(--night);
    font-family: "Josefin Sans", sans-serif;
    font-weight: 300;
    color: var(--ink);
    text-align: center;
  }
  .scene-art {
    position: absolute; left: 0; right: 0; top: 70px; height: 740px;
    background:
      radial-gradient(ellipse 55% 30% at 45% 28%, var(--nebula), transparent 75%),
      radial-gradient(ellipse 75% 30% at 55% 72%, var(--ridge), transparent 80%),
      linear-gradient(180deg, var(--sky-top) 0%, var(--sky-mid) 40%, #1c2468 68%, #101650 85%, var(--night) 100%);
  }
  .address {
    position: absolute; top: 28px; left: 0; right: 0;
    display: flex; align-items: center; gap: 14px;
    font-size: 22px; font-weight: 400; letter-spacing: 5px; white-space: nowrap;
  }
  .address::before, .address::after {
    content: ""; flex: 1; height: 1.5px; background: var(--ink);
  }
  .day {
    position: absolute; top: 528px; left: 0; right: 0;
    font-size: 108px; font-weight: 400; letter-spacing: 32px; padding-left: 32px;
    line-height: 1; text-shadow: 0 3px 6px rgba(0,0,0,.6);
  }
  .date {
    position: absolute; top: 640px; left: 0; right: 0;
    font-size: 42px; font-weight: 400; letter-spacing: 9px; padding-left: 9px;
    line-height: 1; text-shadow: 0 3px 6px rgba(0,0,0,.6);
  }
  .brand {
    position: absolute; top: 718px; left: 0; right: 0;
    display: flex; flex-direction: column; align-items: center; gap: 8px;
  }
  .brand-dot {
    width: 36px; height: 36px; border-radius: 50%; background: var(--gold);
  }
  .brand-name { font-size: 18px; font-weight: 400; letter-spacing: 1px; }
  .rule {
    position: absolute; height: 2px; left: 50%; transform: translateX(-50%);
    background: linear-gradient(90deg, transparent, var(--rule) 15%, var(--rule) 85%, transparent);
  }
  .rule-short { top: 796px; width: 190px; }
  .rule-mid { top: 958px; width: 478px; }
  .rule-low { top: 1066px; width: 478px; }
  .floor-label {
    position: absolute; left: 0; right: 0; color: var(--gold);
    font-weight: 400; line-height: 1;
  }
  .club-label { top: 822px; font-size: 31px; }
  .lounge-label { top: 975px; font-size: 23px; }
  .headliner {
    position: absolute; top: 862px; left: 0; right: 0;
    font-size: 88px; font-weight: 300; line-height: 1;
  }
  .residents {
    position: absolute; top: 1006px; left: 0; right: 0;
    font-size: 52px; font-weight: 300; line-height: 1;
  }
  .info-band {
    position: absolute; left: 0; right: 0; bottom: 0; height: 66px;
    background: var(--band);
    display: flex; align-items: center; justify-content: center;
    font-size: 14px; font-weight: 400; letter-spacing: .3px;
  }
</style>
</head>
<body>
  <main class="flyer">
    <div class="scene-art" role="img" aria-label="Starry galaxy sky with a floating impossible triangle above moonlit blue mountain peaks"></div>

    <p class="address">4217 MARLOW AVENUE SACRAMENTO</p>

    <h1 class="day">FRIDAY</h1>
    <p class="date">MAY 1-2020</p>

    <div class="brand">
      <span class="brand-dot"></span>
      <span class="brand-name">HARBOR</span>
    </div>

    <div class="rule rule-short"></div>
    <p class="floor-label club-label">CLUB FLOOR</p>
    <h2 class="headliner">DJ VORTAN</h2>
    <div class="rule rule-mid"></div>
    <p class="floor-label lounge-label">RESIDENTS ON THE LOUNGE FLOOR</p>
    <h3 class="residents">DJ RUZO &amp; DJ TAV</h3>
    <div class="rule rule-low"></div>

    <footer class="info-band">WWW.HARBORVENUEHALL.EXAMPLE FOR LIST/VIP INQUIRIES</footer>
  </main>
</body>
</html>
```